" Atendimento médico em consultório/Clinica para mulheres em geral. A clinica contará com três médicas ginecologistas. Inicialmente somente a Dra. Lívia atenderá. O principal valor da Clinica é com o cuidado com a Mulher através de atendimento individual e cuidadoso através de especialistas nas áreas da ginecologia e Obstetricia. Apesar de possuir atendimento Obstétrico, o mesmo não será o principal foco da clinica. "

```html
<!DOCTYPE html>
<html lang="pt-BR">
<head>
<meta charset="utf-8">
<title>Receituário — Ginecologia Aurora</title>
<link rel="stylesheet" href="https://fonts.googleapis.com/css2?family=Crimson+Text:wght@400;600&family=Arimo:wght@400;700&family=Open+Sans:wght@400;600&display=swap">
<style>
  :root {
    --rose: #e06f79;
    --rose-deep: #d4566a;
    --rose-soft: #f2b9be;
    --ink: #1d1d1d;
    --ink-soft: #555;
    --paper: #ffffff;
    --backdrop: #e9e9ea;
    --mark-light: #f6f6f6;
    --mark-mid: #e6e6e6;
  }
  * { margin: 0; padding: 0; box-sizing: border-box; }
  html, body { width: 1200px; height: 1200px; overflow: hidden; }
  body {
    background: var(--backdrop);
    display: flex; align-items: center; justify-content: center;
    font-family: "Open Sans", sans-serif; color: var(--ink);
  }
  .prescription-sheet {
    position: relative;
    width: 760px; height: 1130px;
    background: var(--paper);
    box-shadow: 0 4px 18px rgba(0,0,0,.12);
  }
  .sheet-header {
    position: absolute; top: 40px; left: 44px; right: 44px;
    display: flex; justify-content: space-between; align-items: flex-start;
  }
  .clinic-brand { display: flex; flex-direction: column; align-items: center; margin-top: 12px; }
  .clinic-brand-row { display: flex; align-items: center; gap: 10px; }
  .clinic-dot { width: 22px; height: 22px; border-radius: 50%; background: var(--rose); }
  .clinic-name {
    font-family: "Crimson Text", serif; font-weight: 400;
    font-size: 27px; color: var(--rose); line-height: 1;
  }
  .clinic-doctor {
    font-family: "Crimson Text", serif; font-size: 12px;
    color: var(--rose); margin-top: 4px; letter-spacing: .3px;
  }
  .doctor-credentials {
    font-family: "Crimson Text", serif; font-size: 17px; line-height: 1.1;
    color: var(--ink); margin-top: 12px; margin-right: 36px;
  }
  .patient-fields {
    position: absolute; top: 210px; left: 44px; right: 44px;
    display: flex; align-items: flex-end; gap: 8px;
    font-family: "Arimo", sans-serif; font-weight: 700; font-size: 18px;
  }
  .field-line { border-bottom: 1.6px solid var(--ink); height: 1px; margin-bottom: 5px; }
  .field-line.name { flex: 1; }
  .field-line.date { width: 120px; }
  .sheet-title {
    position: absolute; top: 252px; left: 0; right: 0; text-align: center;
    font-family: "Crimson Text", serif; font-size: 22px; color: var(--ink);
  }
  .brand-watermark {
    position: absolute; top: 310px; left: 120px; width: 560px; height: 580px;
    border-radius: 46% 46% 40% 40%;
    background: radial-gradient(ellipse at 50% 45%, var(--mark-mid) 0%, var(--mark-light) 55%, rgba(255,255,255,0) 75%);
  }
  .sheet-footer {
    position: absolute; bottom: 32px; left: 0; right: 0;
    display: flex; justify-content: center; gap: 22px; align-items: center;
    font-size: 10.5px; color: var(--ink-soft);
  }
  .contact-item { display: flex; align-items: center; gap: 6px; line-height: 1.15; }
  .contact-icon {
    width: 20px; height: 20px; border-radius: 50%;
    background: var(--rose); display: flex; align-items: center; justify-content: center;
  }
  .contact-icon svg { width: 11px; height: 11px; }
  .footer-band {
    position: absolute; bottom: 0; left: 0; right: 0; height: 22px;
    background: linear-gradient(to bottom, var(--rose-deep) 0, var(--rose-deep) 4px, var(--rose-soft) 4px, var(--rose) 100%);
  }
</style>
</head>
<body>
  <article class="prescription-sheet">
    <header class="sheet-header">
      <div class="clinic-brand">
        <div class="clinic-brand-row">
          <span class="clinic-dot"></span>
          <span class="clinic-name">Ginecologia Aurora</span>
        </div>
        <span class="clinic-doctor">Dra. Lívia Rocha Amaral</span>
      </div>
      <div class="doctor-credentials">
        Dra. Lívia Rocha Amaral<br>Ginecologista<br>CRM: 000000
      </div>
    </header>

    <div class="patient-fields">
      <span>Nome</span><span class="field-line name"></span>
      <span>Data</span><span class="field-line date"></span>
    </div>

    <h1 class="sheet-title">Receituário</h1>

    <div class="brand-watermark" role="img" aria-label="Marca da clínica em tom claro como fundo decorativo"></div>

    <footer class="sheet-footer">
      <div class="contact-item">
        <span class="contact-icon"><svg viewBox="0 0 24 24"><path fill="#fff" d="M6.6 10.8a15 15 0 0 0 6.6 6.6l2.2-2.2c.3-.3.7-.4 1-.2 1.1.4 2.3.6 3.6.6.6 0 1 .4 1 1V20c0 .6-.4 1-1 1A17 17 0 0 1 3 4c0-.6.4-1 1-1h3.5c.6 0 1 .4 1 1 0 1.3.2 2.5.6 3.6.1.3 0 .7-.2 1z"/></svg></span>
        <span>(xx) xxxx-xxxx<br>(xx) xxxx-xxxx</span>
      </div>
      <div class="contact-item">
        <span class="contact-icon"><svg viewBox="0 0 24 24"><path fill="#fff" d="M12 2a7 7 0 0 0-7 7c0 5 7 13 7 13s7-8 7-13a7 7 0 0 0-7-7zm0 9.5A2.5 2.5 0 1 1 12 6.5a2.5 2.5 0 0 1 0 5z"/></svg></span>
        <span>R. Seu Endereço<br>Cidade - Bairro</span>
      </div>
      <div class="contact-item">
        <span class="contact-icon"><svg viewBox="0 0 24 24"><path fill="#fff" d="M3 5h18v14H3zm2 2v.5l7 4.5 7-4.5V7l-7 4.5z"/></svg></span>
        <span>seuemail@email.com</span>
      </div>
      <div class="contact-item">
        <span class="contact-icon"></span>
        <span>Redes Sociais</span>
      </div>
    </footer>
    <div class="footer-band"></div>
  </article>
</body>
</html>
```